Wix Web design for a Residential redevelopment company

I need a website with a modern and elegant feel that will attract investors. I would like for the color scale to include the colors in our logo and also shades of grey for a modern feel. I need a page for property case studies in which each case study includes property before and after photos, an imbeded youtube video and text in the format of a math problem showing the amount the property was bought for -(minus) what the investor got in return -(minus) rehab costs -(minus) taxes and fees =(equals) Net Profit
However instead of there being an equal sign, I want the math problem to go vertically down with an underline for the equals sign.There needs to be an "About us," page, Investor Inquiries page, Contact Us Page, and Case studies page.
For font formatting, we like Corporate Gothic. Please make the website Wix friendly.

When someone clicks on one of the case study pictures, I would like the pictures to pull up in a click or swipe to the right manner similar to how pictures are structured on brindlo or vexoma.com

Target Market(s)

Investors

Industry/Entity Type

Real Estate

Number of Pages Required

5+ page

Other font styles liked:
• Gothic Corporate

Requirements
Nice to have
• stock photos for the home page

```html
<!DOCTYPE html>
<html lang="en">
<head>
<meta charset="utf-8">
<title>Vantor Property Solutions</title>
<link href="https://fonts.googleapis.com/css2?family=Montserrat:wght@400;500;600&family=Arimo:wght@400;700&display=swap" rel="stylesheet">
<style>
:root{
  --green:#3fa22a;
  --green-dark:#2e8a1e;
  --blue:#1a62c9;
  --blue-dark:#124da3;
  --ink:#2b2b2b;
  --grey-bg:#f3f3f3;
  --line:#d9d9d9;
  --muted:#555;
  --link-blue:#1a7fd6;
}
*{margin:0;padding:0;box-sizing:border-box}
html,body{width:800px;height:1200px;overflow:hidden}
body{position:relative;font-family:"Arimo",Arial,sans-serif;color:var(--ink);background:var(--grey-bg)}
.abs{position:absolute}

/* hero */
.hero{left:0;top:0;width:800px;height:352px;background:linear-gradient(180deg,#6d8a4a 0%,#8a7a5c 40%,#b39a74 60%,#4f8a35 80%,#6aa043 100%)}
.brand{left:96px;top:0;width:74px;height:78px;background:#fff;display:flex;flex-direction:column;align-items:center;justify-content:center;gap:4px}
.brand-mark{width:22px;height:22px;border-radius:50%;background:var(--green)}
.brand-name{font-family:"Montserrat",sans-serif;font-weight:600;font-size:8px;color:var(--green);text-align:center;line-height:1.2}
.nav{left:236px;top:33px;display:flex;gap:16px;font-family:"Montserrat",sans-serif;font-size:6.5px;font-weight:600;color:#fff;letter-spacing:.2px}
.nav-btn{top:30px;height:17px;font-family:"Montserrat",sans-serif;font-size:6.5px;font-weight:600;color:#fff;display:flex;align-items:center;justify-content:center}
.login{left:591px;width:49px;background:var(--blue)}
.register{left:645px;width:58px;background:var(--green)}
.tab{top:162px;height:22px;width:80px;font-family:"Montserrat",sans-serif;font-size:9px;color:#fff;display:flex;align-items:center;justify-content:center}
.tab-buy{left:148px;background:var(--green)}
.tab-sell{left:228px;background:var(--blue)}
.search-box{left:148px;top:184px;width:504px;height:37px;background:#fff}
.search-input{left:164px;top:192px;width:400px;height:21px;border:1px solid var(--line);font-family:"Montserrat",sans-serif;font-size:7px;color:#999;padding-left:7px;display:flex;align-items:center;letter-spacing:.3px}
.search-btn{left:573px;top:192px;width:64px;height:21px;background:var(--green);color:#fff;font-family:"Montserrat",sans-serif;font-size:8px;display:flex;align-items:center;justify-content:center}
.adv{left:149px;top:222px;width:116px;height:20px;background:var(--green);color:#fff;font-family:"Montserrat",sans-serif;font-size:6.5px;display:flex;align-items:center;justify-content:center;gap:6px;letter-spacing:.3px}

/* recently added */
.section-title{left:0;top:382px;width:800px;text-align:center;font-family:"Montserrat",sans-serif;font-weight:500;font-size:17px;color:var(--ink);letter-spacing:.5px}
.title-rule{left:383px;top:409px;width:34px;height:1px;background:var(--green)}
.card{top:434px;width:397px;height:358px;background:#fff;border:1px solid #e4e4e4}
.photo{position:absolute;top:0;width:198px;height:135px}
.photo-before-1{background:linear-gradient(160deg,#9fb0b8,#5b5a55 60%,#6f7a52)}
.photo-after-1{background:linear-gradient(160deg,#e6ecef,#6a6a66 55%,#5f8c3a)}
.photo-before-2{background:linear-gradient(160deg,#8a877d,#4b4640 60%,#3b342c)}
.photo-after-2{background:linear-gradient(160deg,#f2f2f0,#c9c3b8 60%,#a9a090)}
.tag{position:absolute;top:0;background:#111;color:#fff;font-size:10px;padding:2px 5px 3px;font-family:"Arimo",sans-serif}
.price{position:absolute;right:0;top:115px;width:56px;height:20px;background:rgba(79,168,54,.92);color:#fff;font-family:"Montserrat",sans-serif;font-size:10px;display:flex;align-items:center;justify-content:center}
.row{position:absolute;left:14px;width:367px;height:32px;border-bottom:1px solid var(--line);font-size:9px;display:flex;align-items:center}
.row .label{flex:1;padding-left:1px}
.row .val{width:60px;text-align:right;color:#111}
.row .op{width:17px;text-align:right;font-weight:700}
.row.total .label,.row.total .val{font-weight:700}
.row.total .label{padding-left:4px;color:#111}
.row.total .val{color:var(--link-blue);font-weight:400}
.buy-now{position:absolute;left:279px;top:306px;width:102px;height:32px;background:var(--blue);color:#fff;font-family:"Montserrat",sans-serif;font-size:12px;display:flex;align-items:center;justify-content:center}
.see-more{left:315px;top:820px;width:158px;height:26px;background:var(--green);color:#fff;font-family:"Montserrat",sans-serif;font-size:7.5px;font-weight:500;display:flex;align-items:center}
.see-more span{flex:1;text-align:center}
.see-more i{width:27px;height:26px;border-left:1px solid rgba(255,255,255,.6);display:flex;align-items:center;justify-content:center}

/* contact band */
.contact{left:0;top:888px;width:800px;height:106px;background:linear-gradient(90deg,#e9ebe9,#dfe2df 60%,#e7e9e7)}
.contact h2{position:absolute;left:119px;top:37px;font-family:"Montserrat",sans-serif;font-weight:500;font-size:15px;color:#111}
.contact p{position:absolute;left:119px;top:57px;font-size:7.5px;color:#333}
.phone-btn{position:absolute;left:551px;top:41px;width:131px;height:26px;background:var(--blue);color:#fff;font-family:"Montserrat",sans-serif;font-size:12px;display:flex;align-items:center;justify-content:center}

/* footer */
.footer{left:0;top:994px;width:800px;height:206px;background:#fff}
.col{position:absolute;top:40px}
.col h3{font-family:"Montserrat",sans-serif;font-size:7px;font-weight:500;color:var(--green);margin-bottom:8px}
.col li{list-style:none;font-size:6.3px;color:#333;line-height:15px}
.col li.more{color:var(--green)}
.foot-rule{position:absolute;left:96px;top:159px;width:608px;height:1px;background:#eee}
.copy{position:absolute;left:96px;top:174px;font-size:5.5px;color:#555}
.social{position:absolute;top:168px;width:15px;height:15px;border-radius:50%}
</style>
</head>
<body>

<section class="abs hero" role="img" aria-label="Photograph of a large stone craftsman-style house with a green lawn and trees"></section>

<div class="abs brand"><div class="brand-mark"></div><div class="brand-name">Vantor<br>Property</div></div>

<nav class="abs nav"><span>HOME</span><span>BUY</span><span>ABOUT US</span><span>INVESTOR INQUIRIES</span><span>HOW IT WORKS</span><span>CASE STUDIES</span></nav>
<div class="abs nav-btn login">LOGIN</div>
<div class="abs nav-btn register">REGISTER</div>

<svg class="abs" style="left:95px;top:188px" width="28" height="28" viewBox="0 0 28 28"><circle cx="14" cy="14" r="12" fill="none" stroke="#fff" stroke-width="1.5"/><path d="M16 8l-6 6 6 6" fill="none" stroke="#fff" stroke-width="1.5"/></svg>
<svg class="abs" style="left:676px;top:188px" width="28" height="28" viewBox="0 0 28 28"><circle cx="14" cy="14" r="12" fill="none" stroke="#fff" stroke-width="1.5"/><path d="M12 8l6 6-6 6" fill="none" stroke="#fff" stroke-width="1.5"/></svg>

<div class="abs tab tab-buy">BUY</div>
<div class="abs tab tab-sell">SELL</div>
<div class="abs search-box"></div>
<div class="abs search-input">CITY, STATE, ZIP CODE</div>
<div class="abs search-btn">SEARCH</div>
<div class="abs adv">ADVANCED SEARCH <svg width="11" height="11" viewBox="0 0 11 11"><circle cx="5.5" cy="5.5" r="4.8" fill="none" stroke="#fff"/><path d="M4.5 3.3l2.2 2.2-2.2 2.2" fill="none" stroke="#fff"/></svg></div>

<h1 class="abs section-title">RECENTLY ADDED</h1>
<div class="abs title-rule"></div>
<svg class="abs" style="left:15px;top:380px" width="28" height="28" viewBox="0 0 28 28"><circle cx="14" cy="14" r="12.5" fill="none" stroke="#3fa22a" stroke-width="1.5"/><path d="M16 8l-6 6 6 6" fill="none" stroke="#3fa22a" stroke-width="1.5"/></svg>
<svg class="abs" style="left:756px;top:380px" width="28" height="28" viewBox="0 0 28 28"><circle cx="14" cy="14" r="12.5" fill="none" stroke="#3fa22a" stroke-width="1.5"/><path d="M12 8l6 6-6 6" fill="none" stroke="#3fa22a" stroke-width="1.5"/></svg>

<article class="abs card" style="left:0">
  <div class="photo photo-before-1" style="left:0" role="img" aria-label="Before photo: dated house exterior"></div>
  <div class="photo photo-after-1" style="left:198px;width:199px" role="img" aria-label="After photo: renovated modern house exterior"></div>
  <span class="tag" style="left:0">before</span>
  <span class="tag" style="left:198px">after</span>
  <span class="price">400,000</span>
  <div class="row" style="top:135px"><span class="label">amount the property was bought</span><span class="val">200,000</span><span class="op"></span></div>
  <div class="row" style="top:167px"><span class="label">what the investor got in return</span><span class="val">100,000</span><span class="op">–</span></div>
  <div class="row" style="top:199px"><span class="label">rehab costs</span><span class="val">10,000</span><span class="op">–</span></div>
  <div class="row" style="top:231px"><span class="label">taxes and fees</span><span class="val">11,000</span><span class="op">–</span></div>
  <div class="row total" style="top:263px"><span class="label">NET PROFIT</span><span class="val">7,800</span><span class="op"></span></div>
  <div class="buy-now">BUY NOW</div>
</article>

<article class="abs card" style="left:403px">
  <div class="photo photo-before-2" style="left:0" role="img" aria-label="Before photo: empty unfinished interior"></div>
  <div class="photo photo-after-2" style="left:198px;width:199px" role="img" aria-label="After photo: bright renovated living and dining room"></div>
  <span class="tag" style="left:0">before</span>
  <span class="tag" style="left:198px">after</span>
  <span class="price">400,000</span>
  <div class="row" style="top:135px"><span class="label">amount the property was bought</span><span class="val">200,000</span><span class="op"></span></div>
  <div class="row" style="top:167px"><span class="label">what the investor got in return</span><span class="val">100,000</span><span class="op">–</span></div>
  <div class="row" style="top:199px"><span class="label">rehab costs</span><span class="val">10,000</span><span class="op">–</span></div>
  <div class="row" style="top:231px"><span class="label">taxes and fees</span><span class="val">11,000</span><span class="op">–</span></div>
  <div class="row total" style="top:263px"><span class="label">NET PROFIT</span><span class="val">7,800</span><span class="op"></span></div>
  <div class="buy-now">BUY NOW</div>
</article>

<div class="abs see-more"><span>SEE MORE PROPERTIES</span><i><svg width="14" height="14" viewBox="0 0 14 14"><circle cx="7" cy="7" r="6" fill="none" stroke="#fff"/><path d="M6 4.3l2.7 2.7L6 9.7" fill="none" stroke="#fff"/></svg></i></div>

<section class="abs contact">
  <h2>CONTACT US FOR MORE INFORMATION</h2>
  <p>Aenean eu leo quam. Pellentesque ornare sem lacinia quam venenatis vestibulum.</p>
  <div class="phone-btn">014-2786-530</div>
</section>

<footer class="abs footer">
  <div class="col" style="left:96px"><h3>Real Estate</h3><ul><li>Browse all homes</li><li>Albuquerque real estate</li><li>Atlanta real estate</li><li>Austin real estate</li><li>Baltimore real estate</li><li class="more">more</li></ul></div>
  <div class="col" style="left:252px"><h3>Rentals</h3><ul><li>Rental Buildings</li><li>Atlanta apartments for rent</li><li>Austin apartments for rent</li><li>Baltimore apartments for rent</li><li>Boston apartments for rent</li><li class="more">more</li></ul></div>
  <div class="col" style="left:408px"><h3>Properties Categories</h3><ul><li>Homes</li><li>Apartment</li><li>Office</li><li>Hotel</li><li>Condominium</li><li class="more">more</li></ul></div>
  <div class="col" style="left:565px"><h3>Browse Home</h3><ul><li>California</li><li>Texas</li><li>New York</li><li>Florida</li><li>Illinois</li><li class="more">more</li></ul></div>
  <div class="foot-rule"></div>
  <div class="copy">All rights reserved 2018.</div>
  <span class="social" style="left:644px;background:#4aa3e0"></span>
  <span class="social" style="left:666px;background:#3b5a9a"></span>
  <span class="social" style="left:688px;background:#3f7fb8"></span>
</footer>

</body>
</html>
```